Online Psychiatry business - Business Card

I need a business card design. The target audience is busy professionals of any field (this therapy appeals best to 24-35 year olds). It involves psychiatry by tele-medicine (or video-conference). Nothing on it should be a giveaway that it's about mental health. Professional design with silver or gold as the primary colors appeals to me. The card must be as simple and as uncluttered as possible. Some color and flowing design on the edge of the card appeals to me.
CrestMindLink.com should probably appear in the center of the card and stand out, i.e. bold lettering, and easy to read, no cursive, but Ariel Black. Some where below this, should appear "Too Busy to Take Care of Yourself? Think again." Since this isn't office based, I don't think an office address is necessary and limits clutter.
Information that does need to appear is my name: Gerald Whitcombe, MD
General phone number: 541-876-2209. I'm hoping to get an 24-hour answering service soon so leave a little room for this. In addition I want to include two email addresses:
CrestMindLink@maildrop-box.com and CrestMind247@maildrop-box.com
Updates

I like the designs. I would like someone to put the website in bold in the center

 as most have been doing with a smaller font reminder nearby saying "No time" etc.
but I'd like to put my name down in the corner with the rest of the contact material.
Black print against a white or grey background appeals to me, with darker silver artwork near the sides (simple abstract, like wavy lines or something you can one up with that works. 
thanks

I ve tried to provide as much feedback as possible given my time limits, so if you have extra questions, please feel free to email. I tried to attach a file of a business card I really like but make be difficult to actually manufacture. I'm going to send you a link to the photo. The card has a pull tab. There is not much information on the outside. In fact, if you were to design the outside, I would just print : Too Busy to Take Care of Yourself? Think Again.

When you pull the tab the remaining information is on the bottom half of the card. Please don't use the color pink!!!!
http://www.layoutgallerypost.com/2009/05/100-clever-card-ideas/
It is the 39th photo on the list, about 2/3ds of the way down the page. It is titled: Faltenkästli

#7 and #16 have an appeal to me, except for the dot patterns
Hope this helps

I'm running out of time and energy. I 've been trying to give do down the list and give  individual feedback but I won't be able to do that anymore.

So if you have any specific questions, write me, and again thank you for all your effort!!

I know i received your files, including your zip files, Plonix,

but Gideon, did you send me the files including ZIP on project 5914386?
thanks

Target Market(s)

Working professionals and executive, attorneys, etc.

Industry/Entity Type

Business

Logo Text

Don't Have Time to Take Care of Yourself? Think Again.

Logo styles of interest
Pictorial/Combination Logo
Wordmark Logo
Other font styles liked:
• Ariel Black appeals to me the most

Requirements
Must have
• Want to emphasize that the website must be obvious, easily found (The CrestMindLink.com)
For that reason i'd like the card to be white, and minimal decoration on one or both sides just to add some style and color
Nice to have
• A Very uncluttered, elegant design, and something that makes it stick in your head-doesn't everyone want the last?
Should not have
• Nothing on the card that give it away that this is about psychiatry, such as brain or other symbol, but also nothing that gives it away as a medical business, such as a stethoscope or red cross or anything.

```html
<!DOCTYPE html>
<html lang="en">
<head>
<meta charset="utf-8">
<title>CrestMindLink Business Card</title>
<link rel="stylesheet" href="https://fonts.googleapis.com/css2?family=Archivo+Black&family=Mulish:wght@400&display=swap">
<style>
  :root {
    --page: #ffffff;
    --ink: #1e1e1e;
    --accent-red: #e3241b;
    --card-white: #ffffff;
    --card-grey: #6d6e70;
    --contact-text: #ececec;
    --band-dark: #1a1a1a;
    --band-light: #ffffff;
  }
  * { margin: 0; padding: 0; box-sizing: border-box; }
  html, body {
    width: 1018px;
    height: 1200px;
    overflow: hidden;
    background: var(--page);
  }
  .sheet {
    position: relative;
    width: 1018px;
    height: 1200px;
  }
  .card {
    position: absolute;
    left: 45px;
    width: 925px;
    height: 528px;
    overflow: hidden;
    box-shadow: 2px 4px 6px rgba(0, 0, 0, 0.35);
  }
  .card--front { top: 26px; background: var(--card-white); }
  .card--back  { top: 648px; background: var(--card-grey); }

  .tagline {
    position: absolute;
    top: 236px;
    left: 0;
    width: 100%;
    text-align: center;
    font-family: "Mulish", sans-serif;
    font-weight: 400;
    font-size: 33px;
    letter-spacing: 0.2px;
    color: var(--ink);
  }
  .tagline__accent { color: var(--accent-red); }

  .edge-band {
    position: absolute;
    left: 0;
    bottom: 0;
    width: 100%;
    height: 94px;
  }
  .edge-band--dark {
    background: linear-gradient(to bottom, var(--card-white) 0%, #8a8a8a 45%, var(--band-dark) 100%);
  }
  .edge-band--light {
    background: linear-gradient(to bottom, var(--card-grey) 0%, #b6b7b8 45%, var(--band-light) 100%);
  }

  .website {
    position: absolute;
    top: 150px;
    left: 0;
    width: 100%;
    text-align: center;
    font-family: "Archivo Black", "Arial Black", sans-serif;
    font-weight: 400;
    font-size: 48px;
    color: var(--card-white);
  }
  .contact {
    position: absolute;
    top: 263px;
    right: 73px;
    text-align: right;
    list-style: none;
    font-family: "Mulish", sans-serif;
    font-size: 22px;
    line-height: 36px;
    color: var(--contact-text);
  }
</style>
</head>
<body>
<main class="sheet">
  <section class="card card--front" aria-label="Card front">
    <p class="tagline">Too Busy to Take Care of Yourself? <span class="tagline__accent">Think again</span></p>
    <div class="edge-band edge-band--dark" role="img" aria-label="Dark decorative border along the bottom edge"></div>
  </section>

  <section class="card card--back" aria-label="Card back">
    <h1 class="website">CrestMindLink.com</h1>
    <ul class="contact">
      <li>Gerald Whitcombe, MD</li>
      <li>P - 541-876-2209</li>
      <li>E - CrestMindLink@maildrop-box.com</li>
      <li>CrestMind247@maildrop-box.com</li>
    </ul>
    <div class="edge-band edge-band--light" role="img" aria-label="Light decorative border along the bottom edge"></div>
  </section>
</main>
</body>
</html>
```